Group fitness classes - DL flyer

We need a flyer design for our boutique fitness studio.

We would prefer to see the use of pictures in the design.

One sided. Please allow space around the edges for bleed.

Flyer should have the following text:

Harwell Motion Loft
Group fitness special – two weeks unlimited group fitness classes for $29*
Enjoy unlimited access to our fantastic group classes including PulseRun, Yoga, Strength Circuit and Self Defence Martial Arts.
Purchase your pass through our online store by selecting the "Special Offers" option.
Bring this flyer to your first class and receive an extra two weeks free!

www.harwellmotionloft.com.au
or phone
0482 *** ***
4/63 Birchwood Lane Flemington

*New clients only

Industry/Entity Type

Boutique

Font styles to use
Serif
Sans Serif

Requirements
Must have
• Photos
Should not have
• Cartoons

```html
<!DOCTYPE html>
<html lang="en">
<head>
<meta charset="utf-8">
<title>Harwell Motion Loft – Group Fitness Special</title>
<link rel="stylesheet" href="https://fonts.googleapis.com/css2?family=Oswald:wght@500;700&family=Great+Vibes&family=Roboto+Condensed:wght@400;700&display=swap">
<style>
  :root{
    --red:#c8102e;
    --red-dark:#8e0a1f;
    --gold:#c9a227;
    --ink:#1d1d1f;
    --grey:#dcdcdc;
    --grey-dark:#4a4a4a;
    --paper:#f6f6f6;
  }
  html,body{margin:0;padding:0;overflow:hidden;}
  body{width:855px;height:1200px;}
  .flyer{
    position:relative;width:855px;height:1200px;overflow:hidden;
    background:radial-gradient(ellipse at 50% 55%,#ffffff 0%,var(--paper) 60%,#e4e4e4 100%);
    font-family:"Roboto Condensed",Arial,sans-serif;color:var(--ink);
  }
  .swoosh{position:absolute;left:0;top:0;width:855px;height:1200px;}
  .brand{
    position:absolute;top:34px;left:0;width:100%;text-align:center;
    font-family:"Oswald",sans-serif;font-weight:700;font-size:44px;letter-spacing:3px;
    color:#ffffff;text-transform:uppercase;
  }
  .photo{position:absolute;border-radius:50%;border:8px solid #fff;box-shadow:0 6px 18px rgba(0,0,0,.3);}
  .photo--left{left:70px;top:215px;width:250px;height:250px;background:radial-gradient(circle at 50% 40%,#d6b49a,#4b6d8c 70%,#2a3f57);}
  .photo--centre{left:245px;top:195px;width:360px;height:360px;background:radial-gradient(circle at 50% 40%,#e7d9c8,#a0a9b3 55%,#4d5966);z-index:2;}
  .photo--right{left:540px;top:225px;width:250px;height:250px;background:radial-gradient(circle at 50% 40%,#d9c0a8,#8b8f96 60%,#3a3f47);}
  .headline{
    position:absolute;top:605px;left:0;width:100%;text-align:center;margin:0;
    font-family:"Oswald",sans-serif;font-weight:700;font-size:98px;line-height:1;
    text-transform:uppercase;color:var(--red);letter-spacing:1px;
    text-shadow:0 3px 0 var(--red-dark),0 6px 10px rgba(0,0,0,.25);
  }
  .special{
    position:absolute;top:690px;left:50%;transform:translateX(-50%);
    font-family:"Great Vibes",cursive;font-size:90px;line-height:1;color:var(--gold);
    text-shadow:0 2px 3px rgba(0,0,0,.3);white-space:nowrap;
  }
  .price{position:absolute;left:62px;top:772px;width:250px;}
  .price__tag{
    display:inline-block;background:#fff;border:4px solid var(--red);border-radius:14px;
    padding:0 16px;font-family:"Oswald",sans-serif;font-weight:700;color:var(--red);
    font-size:28px;line-height:1.25;transform:rotate(-4deg);position:relative;z-index:2;margin-left:18px;
  }
  .price__tag b{font-size:52px;vertical-align:-5px;}
  .price__box{
    margin-top:-10px;background:var(--red);color:#fff;border-radius:14px;padding:18px 12px 10px;
    font-family:"Oswald",sans-serif;font-weight:700;font-size:25px;line-height:1.05;text-align:center;
    text-transform:uppercase;box-shadow:0 5px 12px rgba(0,0,0,.3);
  }
  .couple{
    position:absolute;left:320px;top:785px;width:250px;height:178px;
    background:linear-gradient(180deg,#f2f2f2,#cfd3d8 70%,#5c7fa8);
  }
  .badge{position:absolute;left:590px;top:758px;width:210px;height:210px;}
  .badge svg{position:absolute;inset:0;width:100%;height:100%;}
  .badge p{
    position:absolute;inset:46px 34px;margin:0;display:flex;align-items:center;justify-content:center;
    text-align:center;color:#fff;font-weight:700;font-size:19px;line-height:1.2;
  }
  .info{position:absolute;top:976px;left:0;width:100%;text-align:center;}
  .info p{margin:0;font-size:23px;line-height:1.27;}
  .info .classes{color:var(--red);font-weight:700;text-transform:uppercase;}
  .info strong{color:var(--red);text-transform:uppercase;}
  .footer{
    position:absolute;left:0;bottom:0;width:100%;height:100px;
    background:linear-gradient(180deg,#e9e9e9,var(--grey));
    border-top:6px solid var(--red);text-align:center;color:var(--grey-dark);
  }
  .footer__name{margin:8px 0 2px;font-family:"Oswald",sans-serif;font-weight:500;font-size:22px;letter-spacing:3px;text-transform:uppercase;color:var(--red);}
  .footer__address{margin:0;font-size:20px;display:flex;justify-content:center;align-items:center;gap:8px;}
  .footer__contact{margin:3px 0 0;font-size:20px;font-weight:700;display:flex;justify-content:center;align-items:center;gap:10px;}
  .icon{width:20px;height:20px;fill:var(--red);}
</style>
</head>
<body>
<div class="flyer">
  <svg class="swoosh" viewBox="0 0 855 1200" aria-hidden="true">
    <defs>
      <linearGradient id="redBand" x1="0" y1="0" x2="1" y2="0">
        <stop offset="0" stop-color="#8e0a1f"/>
        <stop offset=".5" stop-color="#d41a3a"/>
        <stop offset="1" stop-color="#8e0a1f"/>
      </linearGradient>
    </defs>
    <path d="M0 0 H855 V250 C700 160 560 300 420 230 C280 160 140 250 0 200 Z" fill="url(#redBand)"/>
    <path d="M0 200 C140 250 280 160 420 230 C560 300 700 160 855 250 V280 C700 200 560 330 420 262 C280 195 140 280 0 232 Z" fill="#e9a0ad" opacity=".7"/>
    <path d="M0 560 C200 520 400 600 855 520 V620 C500 650 250 580 0 640 Z" fill="#f0c9d1" opacity=".5"/>
  </svg>

  <div class="brand">Harwell Motion Loft</div>

  <div class="photo photo--left" role="img" aria-label="Photo: woman training with a fitness ball"></div>
  <div class="photo photo--centre" role="img" aria-label="Photo: group fitness class working out on exercise balls"></div>
  <div class="photo photo--right" role="img" aria-label="Photo: class members lifting weights in the studio"></div>

  <h1 class="headline">Group Fitness</h1>
  <div class="special">Special</div>

  <div class="price">
    <div class="price__tag">JUST <b>$29</b></div>
    <div class="price__box">Two weeks unlimited group fitness classes</div>
  </div>

  <div class="couple" role="img" aria-label="Photo: man and woman in sportswear stretching on the floor"></div>

  <div class="badge">
    <svg viewBox="-100 -100 200 200" aria-hidden="true">
      <polygon fill="#c8102e" stroke="#8e0a1f" stroke-width="2" points="100,0 85,23 87,50 62,62 50,87 23,85 0,100 -23,85 -50,87 -62,62 -87,50 -85,23 -100,0 -85,-23 -87,-50 -62,-62 -50,-87 -23,-85 0,-100 23,-85 50,-87 62,-62 87,-50 85,-23"/>
    </svg>
    <p>Bring this flyer to your first class and receive an extra two weeks FREE!</p>
  </div>

  <div class="info">
    <p>Enjoy unlimited access to our <strong>fantastic group classes</strong> including:</p>
    <p class="classes">PulseRun / Yoga / Strength Circuit &amp; Self Defence Martial Arts.</p>
    <p>Purchase your PASS through our online store by selecting the “Special Offers” option.</p>
  </div>

  <footer class="footer">
    <p class="footer__name">Harwell Motion Loft</p>
    <p class="footer__address">
      <svg class="icon" viewBox="0 0 24 24" aria-hidden="true"><path d="M12 2a7 7 0 0 0-7 7c0 5 7 13 7 13s7-8 7-13a7 7 0 0 0-7-7zm0 9.5a2.5 2.5 0 1 1 0-5 2.5 2.5 0 0 1 0 5z"/></svg>
      4/63 Birchwood Lane, Flemington - MELBOURNE, Vic, 3031
    </p>
    <p class="footer__contact">
      <svg class="icon" viewBox="0 0 24 24" aria-hidden="true"><path d="M6.6 10.8a15 15 0 0 0 6.6 6.6l2.2-2.2a1 1 0 0 1 1-.25 11.4 11.4 0 0 0 3.6.6 1 1 0 0 1 1 1V20a1 1 0 0 1-1 1A17 17 0 0 1 3 4a1 1 0 0 1 1-1h3.5a1 1 0 0 1 1 1c0 1.25.2 2.45.6 3.6a1 1 0 0 1-.25 1z"/></svg>
      0482 *** ***
      <span>|</span>
      www.harwellmotionloft.com.au
    </p>
  </footer>
</div>
</body>
</html>
```